"tide-LOOP." SoCal's Fishing Industry's single stop for the latest products, content, and services

Hi, looking for a website design for new LA based company called "tide-LOOP." Where we showcase all the latest and greatest products, services, and content in a highly visually appealing platform for all fishing manufacturers and service providers as they relate to the fishing community (manufactures and service providers pay for cost-tiered content exposure and marketing, free exposure for manufacturers and service providers will have affiliate marketing link at minimal content exposure). As well, looking to include an in-site blog, store-products, and media content such as articles, video edits, and fishing condition picture galleries. Visually, looking for a minimalist/clean/blocked/ filterable and visually captivating gallery. Looking for a color pallet with white-background, deep blue- primary, light gray- secondary, light sky blue- third. Style- cleanliness and structure of wirestack.example meets content like mkharborline.example.

Target Market(s)

Primary- Southern California/Southwest Fishing Community, Secondary- All other US Fishing Communities

Coding

Coded - Design and coding required

Number of Pages Required

5+ page

Font styles to use
Sans Serif

Colors
959595
86cfc6
cadf82
333333
0555a3

Requirements
Must have
• Fast loading, mobile friendly, Analytics page, email sign up link for emailed newsletter (that is not a full page pop-up but integrated into browse bar), integrated social media links, search bar, filter link, home page return link, minimalist and clean design. Formatted to product showcase website style- please see attached files for ideas for design format and word-logo.
Should not have
• No Clutter, No background advertisements, No long text scripts outside of products main page,

```html
<!DOCTYPE html>
<html lang="en">
<head>
<meta charset="utf-8">
<title>tide-LOOP. | Fishing Products, Content &amp; Services</title>
<link href="https://fonts.googleapis.com/css2?family=Lato:wght@300;400;700;900&family=Roboto:wght@400;500;700&display=swap" rel="stylesheet">
<style>
  :root {
    --blue: #0a8ad6;
    --ink: #111111;
    --text: #333333;
    --muted: #959595;
    --pill-gray: #bdbdbd;
    --panel: #ececec;
    --band: #e6e6e6;
    --white: #ffffff;
    --yellow: #f7c416;
    --card-border: #5aaee6;
  }
  * { box-sizing: border-box; margin: 0; padding: 0; }
  html, body { width: 1200px; height: 2384px; overflow: hidden; background: var(--white); }
  body { position: relative; font-family: "Roboto", Arial, sans-serif; color: var(--text); }

  /* Hero */
  .hero { position: absolute; left: 0; top: 0; width: 1200px; height: 680px; overflow: hidden; }
  .hero-photo {
    position: absolute; inset: 0;
    background:
      linear-gradient(rgba(15,15,15,.32), rgba(15,15,15,.32)),
      radial-gradient(ellipse 40% 18% at 25% 50%, rgba(190,120,40,.55), transparent 70%),
      radial-gradient(ellipse 35% 16% at 80% 40%, rgba(170,90,30,.5), transparent 70%),
      linear-gradient(180deg,
        #8a8c8e 0%, #7c7f80 9%,
        #5d5a3a 14%, #8a6a2c 22%, #6e5a26 30%, #4a4a2a 38%, #3f452e 44%,
        #8d9296 47%, #7d8286 55%, #6a6f73 62%,
        #2b2a27 68%, #3a3833 76%, #2a2825 86%, #4b4f52 93%, #3b3e41 100%);
  }
  .hero-title {
    position: absolute; top: 246px; width: 100%; text-align: center;
    font-family: "Lato", Arial, sans-serif; font-weight: 900; font-size: 74px; line-height: 84px; color: var(--white);
  }
  .hero-lede {
    position: absolute; top: 325px; width: 100%; text-align: center;
    font-family: "Lato", Arial, sans-serif; font-size: 19px; line-height: 24px; color: var(--white);
  }
  .hero-cta {
    position: absolute; left: 524px; top: 394px; width: 135px; height: 38px; border-radius: 19px;
    background: var(--blue); color: var(--white); font-family: "Lato", Arial, sans-serif; font-size: 14px;
    display: flex; align-items: center; justify-content: center; letter-spacing: .3px;
  }
  .hero-indicator {
    position: absolute; left: 521px; top: 461px; width: 130px; height: 16px; border-radius: 8px 8px 0 0;
    background: rgba(255,255,255,.7);
  }
  .hero-arrow {
    position: absolute; top: 380px; width: 24px; height: 24px; border-radius: 50%; background: var(--blue);
    display: flex; align-items: center; justify-content: center;
  }
  .hero-arrow.prev { left: 45px; }
  .hero-arrow.next { left: 1122px; }

  /* Navigation */
  .nav {
    position: absolute; left: 51px; top: 44px; width: 1093px; height: 64px; border-radius: 32px;
    background: var(--white); display: flex; align-items: center; padding: 0 22px 0 30px;
    font-family: "Lato", Arial, sans-serif;
  }
  .brand { font-weight: 900; font-size: 27px; color: var(--ink); margin-right: 28px; letter-spacing: -.3px; }
  .nav-link { font-size: 16px; color: var(--ink); margin-right: 18px; display: flex; align-items: center; gap: 5px; }
  .nav-link::after { content: ""; border: 4px solid transparent; border-top: 5px solid var(--ink); margin-top: 5px; }
  .search {
    width: 495px; height: 26px; border-radius: 13px; background: #ebebeb; margin-left: 2px;
    display: flex; align-items: center; justify-content: space-between; padding: 0 12px 0 18px;
    font-size: 10px; color: #b3b3b3;
  }
  .nav-actions { display: flex; align-items: center; gap: 8px; margin-left: auto; }
  .btn-blog { background: #7a7a7a; color: var(--white); border-radius: 13px; height: 26px; padding: 0 14px; font-size: 14px; display: flex; align-items: center; }
  .btn-signup { background: var(--blue); color: var(--white); border-radius: 13px; height: 26px; padding: 0 13px; font-size: 14px; display: flex; align-items: center; margin-left: 4px; }
  .social { display: flex; gap: 4px; }
  .social span { width: 18px; height: 18px; border-radius: 50%; background: var(--blue); display: block; }

  /* Sections */
  .band-gray { position: absolute; left: 0; top: 1212px; width: 1200px; height: 528px; background: var(--band); }
  .shelf { position: absolute; left: 87px; width: 1030px; }
  .shelf-head {
    height: 52px; border-radius: 10px 10px 0 0; border: 2px solid #1b7fc4;
    background: linear-gradient(180deg, #4fb7f0 0%, #1c96dd 45%, #0b82cf 100%);
    display: flex; align-items: center; justify-content: space-between; padding: 0 16px 0 28px;
  }
  .shelf-title { font-family: "Lato", Arial, sans-serif; font-size: 26px; font-weight: 400; color: var(--white); }
  .shelf-controls { display: flex; gap: 6px; }
  .ctrl { width: 21px; height: 21px; border-radius: 50%; display: flex; align-items: center; justify-content: center; }
  .ctrl.prev { background: rgba(255,255,255,.45); }
  .ctrl.next { background: var(--white); }
  .cards { display: flex; gap: 22px; margin-top: 11px; }

  /* Product card */
  .card {
    width: 241px; height: 313px; border: 1.5px solid var(--card-border); border-radius: 8px; overflow: hidden;
    background: var(--white); position: relative;
  }
  .card-media { position: relative; height: 206px; }
  .product-photo {
    position: absolute; left: 30px; top: 46px; width: 180px; height: 120px; border-radius: 60px;
    background: radial-gradient(ellipse closest-side, var(--tone) 0%, var(--tone) 38%, var(--tone-2) 70%, rgba(255,255,255,0) 100%);
  }
  .product-photo.wide { left: 18px; top: 70px; width: 205px; height: 70px; }
  .product-photo.tall { left: 70px; top: 40px; width: 100px; height: 130px; }
  .tag-pick {
    position: absolute; left: 16px; top: 14px; height: 18px; padding: 0 8px 0 6px; border-radius: 9px;
    background: var(--ink); color: var(--white); font-size: 7.5px; font-weight: 500; display: flex; align-items: center; gap: 4px;
  }
  .tag-pick b { color: #2a9be0; font-size: 9px; }
  .tag-date {
    position: absolute; right: 16px; top: 14px; width: 52px; height: 18px; border-radius: 9px;
    background: #dcdcdc; color: var(--white); font-size: 7.5px; display: flex; align-items: center; justify-content: center;
  }
  .fav {
    position: absolute; right: 14px; bottom: 10px; width: 20px; height: 20px; border-radius: 50%;
    background: #e2e2e2; display: flex; align-items: center; justify-content: center;
  }
  .card-info { background: var(--panel); height: 105px; padding: 10px 18px 0; }
  .card-title { font-size: 15px; font-weight: 700; color: var(--ink); margin-bottom: 6px; }
  .card-desc { font-size: 10px; line-height: 14px; color: var(--muted); height: 30px; max-width: 186px; }
  .card-buy { display: flex; align-items: center; margin-top: 9px; }
  .price { font-size: 12.5px; color: var(--ink); width: 28px; }
  .btn-cart {
    width: 74px; height: 14px; border-radius: 7px; background: var(--blue); color: var(--white);
    font-size: 5.5px; font-weight: 700; display: flex; align-items: center; justify-content: center; margin-right: 6px;
  }
  .btn-save {
    width: 33px; height: 14px; border-radius: 7px; background: var(--pill-gray); color: var(--white);
    font-size: 5.5px; display: flex; align-items: center; justify-content: center;
  }
  .card.active .card-info { background: var(--blue); }
  .card.active .card-title, .card.active .card-desc, .card.active .price { color: var(--white); }
  .card.active .btn-cart { background: var(--yellow); color: var(--ink); }
  .card.active .btn-save { background: #5bb6ea; }

  /* Footer */
  .footer-bar {
    position: absolute; left: 0; top: 2279px; width: 1200px; height: 46px; background: var(--blue);
    display: flex; align-items: center; justify-content: center;
    font-family: "Lato", Arial, sans-serif; font-size: 14.5px; color: var(--white); letter-spacing: .4px; font-weight: 300;
  }
  .footer-bar .sep { margin: 0 9px; font-weight: 700; }
  .footer-bar .social { margin-left: 22px; gap: 3px; }
  .footer-bar .social span { width: 22px; height: 22px; background: var(--white); }
  .copyright {
    position: absolute; top: 2347px; width: 1200px; text-align: center;
    font-family: "Lato", Arial, sans-serif; font-size: 12px; color: var(--muted);
  }
</style>
</head>
<body>

<header class="hero">
  <div class="hero-photo" role="img" aria-label="Two anglers in folding chairs fishing from a wooden dock on a lake lined with autumn trees"></div>
  <h1 class="hero-title">tide-LOOP.</h1>
  <p class="hero-lede">consectetuer adipiscing elit. Aenean commodo ligula eget dolor. Aenean massa.<br>Cum sociis natoque penatibus et magnis dis parturient montes.</p>
  <a class="hero-cta">NEW STUFF</a>
  <div class="hero-indicator"></div>
  <span class="hero-arrow prev"><svg width="10" height="10" viewBox="0 0 10 10"><path d="M6.5 2 3.5 5l3 3" fill="none" stroke="#fff" stroke-width="1.8"/></svg></span>
  <span class="hero-arrow next"><svg width="10" height="10" viewBox="0 0 10 10"><path d="M3.5 2l3 3-3 3" fill="none" stroke="#fff" stroke-width="1.8"/></svg></span>

  <nav class="nav">
    <span class="brand">tide-LOOP.</span>
    <span class="nav-link">Browse</span>
    <span class="nav-link">More</span>
    <div class="search">
      <span>Search For Products</span>
      <svg width="11" height="11" viewBox="0 0 12 12"><circle cx="5" cy="5" r="3.6" fill="none" stroke="#999" stroke-width="1.5"/><path d="M7.7 7.7 11 11" stroke="#999" stroke-width="1.6"/></svg>
    </div>
    <div class="nav-actions">
      <span class="btn-blog">Blog</span>
      <span class="btn-signup">Sign Up</span>
      <div class="social"><span></span><span></span><span></span></div>
    </div>
  </nav>
</header>

<div class="band-gray"></div>

<!-- Featured -->
<section class="shelf" style="top:755px">
  <div class="shelf-head">
    <h2 class="shelf-title">Featured Products</h2>
    <div class="shelf-controls">
      <span class="ctrl prev"><svg width="8" height="8" viewBox="0 0 10 10"><path d="M6.5 2 3.5 5l3 3" fill="none" stroke="#1c8fd6" stroke-width="2"/></svg></span>
      <span class="ctrl next"><svg width="8" height="8" viewBox="0 0 10 10"><path d="M3.5 2l3 3-3 3" fill="none" stroke="#0b82cf" stroke-width="2"/></svg></span>
    </div>
  </div>
  <div class="cards">
    <article class="card">
      <div class="card-media"><span class="tag-pick"><b>★</b> STAFF PICK</span><span class="tag-date">NOV 16</span>
        <div class="product-photo" style="--tone:#2a2c2e;--tone-2:#8e9194" role="img" aria-label="Black fishing rod holder"></div>
        <span class="fav"><svg width="10" height="9" viewBox="0 0 10 9"><path d="M5 8.2 1.2 4.4a2.2 2.2 0 0 1 3.1-3.1L5 2l.7-.7a2.2 2.2 0 0 1 3.1 3.1z" fill="none" stroke="#555" stroke-width="1"/></svg></span></div>
      <div class="card-info"><h3 class="card-title">Fishing Rod holders...</h3><p class="card-desc">Aliter autem vobis placet. Duarum enim vitarum nobis erunt instituta capienda.</p>
        <div class="card-buy"><span class="price">$35</span><span class="btn-cart">ADD TO CART</span><span class="btn-save">SAVE</span></div></div>
    </article>
    <article class="card">
      <div class="card-media"><span class="tag-pick"><b>★</b> STAFF PICK</span><span class="tag-date">DEC 13</span>
        <div class="product-photo tall" style="--tone:#b07a2e;--tone-2:#dcb67a" role="img" aria-label="Round wooden fishing rod rack"></div>
        <span class="fav"><svg width="10" height="9" viewBox="0 0 10 9"><path d="M5 8.2 1.2 4.4a2.2 2.2 0 0 1 3.1-3.1L5 2l.7-.7a2.2 2.2 0 0 1 3.1 3.1z" fill="none" stroke="#555" stroke-width="1"/></svg></span></div>
      <div class="card-info"><h3 class="card-title">Fishing Rod Racks...</h3><p class="card-desc">Nullus est igitur cuiusquam dies natalis. Primum quid tu dicis breve? Primum</p>
        <div class="card-buy"><span class="price">$45</span><span class="btn-cart">ADD TO CART</span><span class="btn-save">SAVE</span></div></div>
    </article>
    <article class="card active">
      <div class="card-media"><span class="tag-pick"><b>★</b> STAFF PICK</span><span class="tag-date">SEP 17</span>
        <div class="product-photo" style="--tone:#3f6f98;--tone-2:#b9c4cc" role="img" aria-label="Blue and silver spinning reel"></div>
        <span class="fav"><svg width="10" height="9" viewBox="0 0 10 9"><path d="M5 8.2 1.2 4.4a2.2 2.2 0 0 1 3.1-3.1L5 2l.7-.7a2.2 2.2 0 0 1 3.1 3.1z" fill="none" stroke="#555" stroke-width="1"/></svg></span></div>
      <div class="card-info"><h3 class="card-title">Reels...</h3><p class="card-desc">Hunc vos beatum; Tria genera bonorum; Nam ista vestra: Si gravis, brevis;</p>
        <div class="card-buy"><span class="price">$20</span><span class="btn-cart">ADD TO CART</span><span class="btn-save">SAVE</span></div></div>
    </article>
    <article class="card">
      <div class="card-media"><span class="tag-pick"><b>★</b> STAFF PICK</span><span class="tag-date">MAR 11</span>
        <div class="product-photo wide" style="--tone:#c9ccce;--tone-2:#e6e8ea" role="img" aria-label="Silver spoon hard bait with hook"></div>
        <span class="fav"><svg width="10" height="9" viewBox="0 0 10 9"><path d="M5 8.2 1.2 4.4a2.2 2.2 0 0 1 3.1-3.1L5 2l.7-.7a2.2 2.2 0 0 1 3.1 3.1z" fill="none" stroke="#555" stroke-width="1"/></svg></span></div>
      <div class="card-info"><h3 class="card-title">Hard Baits...</h3><p class="card-desc">Is ita vivebat, ut nulla tam exquisita posset inveniri voluptas, qua non abundaret.</p>
        <div class="card-buy"><span class="price">$40</span><span class="btn-cart">ADD TO CART</span><span class="btn-save">SAVE</span></div></div>
    </article>
  </div>
</section>

<!-- Trending -->
<section class="shelf" style="top:1282px">
  <div class="shelf-head">
    <h2 class="shelf-title">Trending</h2>
    <div class="shelf-controls">
      <span class="ctrl prev"><svg width="8" height="8" viewBox="0 0 10 10"><path d="M6.5 2 3.5 5l3 3" fill="none" stroke="#1c8fd6" stroke-width="2"/></svg></span>
      <span class="ctrl next"><svg width="8" height="8" viewBox="0 0 10 10"><path d="M3.5 2l3 3-3 3" fill="none" stroke="#0b82cf" stroke-width="2"/></svg></span>
    </div>
  </div>
  <div class="cards">
    <article class="card">
      <div class="card-media"><span class="tag-pick"><b>★</b> STAFF PICK</span><span class="tag-date">NOV 16</span>
        <div class="product-photo tall" style="--tone:#6c6f72;--tone-2:#d3d5d7" role="img" aria-label="Single fishing hook"></div>
        <span class="fav"><svg width="10" height="9" viewBox="0 0 10 9"><path d="M5 8.2 1.2 4.4a2.2 2.2 0 0 1 3.1-3.1L5 2l.7-.7a2.2 2.2 0 0 1 3.1 3.1z" fill="none" stroke="#555" stroke-width="1"/></svg></span></div>
      <div class="card-info"><h3 class="card-title">Fishing hooks...</h3><p class="card-desc">Aliter autem vobis placet. Duarum enim vitarum nobis erunt instituta capienda.</p>
        <div class="card-buy"><span class="price">$35</span><span class="btn-cart">ADD TO CART</span><span class="btn-save">SAVE</span></div></div>
    </article>
    <article class="card">
      <div class="card-media"><span class="tag-pick"><b>★</b> STAFF PICK</span><span class="tag-date">DEC 13</span>
        <div class="product-photo wide" style="--tone:#1e5a5c;--tone-2:#8fa9aa" role="img" aria-label="Landing net with green handle"></div>
        <span class="fav"><svg width="10" height="9" viewBox="0 0 10 9"><path d="M5 8.2 1.2 4.4a2.2 2.2 0 0 1 3.1-3.1L5 2l.7-.7a2.2 2.2 0 0 1 3.1 3.1z" fill="none" stroke="#555" stroke-width="1"/></svg></span></div>
      <div class="card-info"><h3 class="card-title">Fishing Tools...</h3><p class="card-desc">Nullus est igitur cuiusquam dies natalis. Primum quid tu dicis breve? Primum</p>
        <div class="card-buy"><span class="price">$45</span><span class="btn-cart">ADD TO CART</span><span class="btn-save">SAVE</span></div></div>
    </article>
    <article class="card">
      <div class="card-media"><span class="tag-pick"><b>★</b> STAFF PICK</span><span class="tag-date">SEP 17</span>
        <div class="product-photo tall" style="--tone:#3d3a36;--tone-2:#b3aea8" role="img" aria-label="Jig head hook"></div>
        <span class="fav"><svg width="10" height="9" viewBox="0 0 10 9"><path d="M5 8.2 1.2 4.4a2.2 2.2 0 0 1 3.1-3.1L5 2l.7-.7a2.2 2.2 0 0 1 3.1 3.1z" fill="none" stroke="#555" stroke-width="1"/></svg></span></div>
      <div class="card-info"><h3 class="card-title">Jigs &amp; Rigs...</h3><p class="card-desc">Hunc vos beatum; Tria genera bonorum; Nam ista vestra: Si gravis, brevis;</p>
        <div class="card-buy"><span class="price">$20</span><span class="btn-cart">ADD TO CART</span><span class="btn-save">SAVE</span></div></div>
    </article>
    <article class="card">
      <div class="card-media"><span class="tag-pick"><b>★</b> STAFF PICK</span><span class="tag-date">MAR 11</span>
        <div class="product-photo" style="--tone:#1f3a26;--tone-2:#6fae6a" role="img" aria-label="Rod and reel combo with green accents"></div>
        <span class="fav"><svg width="10" height="9" viewBox="0 0 10 9"><path d="M5 8.2 1.2 4.4a2.2 2.2 0 0 1 3.1-3.1L5 2l.7-.7a2.2 2.2 0 0 1 3.1 3.1z" fill="none" stroke="#555" stroke-width="1"/></svg></span></div>
      <div class="card-info"><h3 class="card-title">Rod &amp; Reel Combos...</h3><p class="card-desc">Is ita vivebat, ut nulla tam exquisita posset inveniri voluptas, qua non abundaret.</p>
        <div class="card-buy"><span class="price">$40</span><span class="btn-cart">ADD TO CART</span><span class="btn-save">SAVE</span></div></div>
    </article>
  </div>
</section>

<!-- New Stuff -->
<section class="shelf" style="top:1813px">
  <div class="shelf-head">
    <h2 class="shelf-title">New Stuff</h2>
    <div class="shelf-controls">
      <span class="ctrl prev"><svg width="8" height="8" viewBox="0 0 10 10"><path d="M6.5 2 3.5 5l3 3" fill="none" stroke="#1c8fd6" stroke-width="2"/></svg></span>
      <span class="ctrl next"><svg width="8" height="8" viewBox="0 0 10 10"><path d="M3.5 2l3 3-3 3" fill="none" stroke="#0b82cf" stroke-width="2"/></svg></span>
    </div>
  </div>
  <div class="cards">
    <article class="card">
      <div class="card-media"><span class="tag-pick"><b>★</b> STAFF PICK</span><span class="tag-date">NOV 16</span>
        <div class="product-photo wide" style="--tone:#26234a;--tone-2:#8d8aa8" role="img" aria-label="Dark blue fishing rod"></div>
        <span class="fav"><svg width="10" height="9" viewBox="0 0 10 9"><path d="M5 8.2 1.2 4.4a2.2 2.2 0 0 1 3.1-3.1L5 2l.7-.7a2.2 2.2 0 0 1 3.1 3.1z" fill="none" stroke="#555" stroke-width="1"/></svg></span></div>
      <div class="card-info"><h3 class="card-title">Rods...</h3><p class="card-desc">Aliter autem vobis placet. Duarum enim vitarum nobis erunt instituta capienda.</p>
        <div class="card-buy"><span class="price">$35</span><span class="btn-cart">ADD TO CART</span><span class="btn-save">SAVE</span></div></div>
    </article>
    <article class="card">
      <div class="card-media"><span class="tag-pick"><b>★</b> STAFF PICK</span><span class="tag-date">DEC 13</span>
        <div class="product-photo wide" style="--tone:#2b2b28;--tone-2:#8f8f88" role="img" aria-label="Dark soft plastic lizard bait"></div>
        <span class="fav"><svg width="10" height="9" viewBox="0 0 10 9"><path d="M5 8.2 1.2 4.4a2.2 2.2 0 0 1 3.1-3.1L5 2l.7-.7a2.2 2.2 0 0 1 3.1 3.1z" fill="none" stroke="#555" stroke-width="1"/></svg></span></div>
      <div class="card-info"><h3 class="card-title">Soft Baits...</h3><p class="card-desc">Nullus est igitur cuiusquam dies natalis. Primum quid tu dicis breve? Primum</p>
        <div class="card-buy"><span class="price">$45</span><span class="btn-cart">ADD TO CART</span><span class="btn-save">SAVE</span></div></div>
    </article>
    <article class="card">
      <div class="card-media"><span class="tag-pick"><b>★</b> STAFF PICK</span><span class="tag-date">SEP 17</span>
        <div class="product-photo" style="--tone:#7a6a3a;--tone-2:#d9b46a" role="img" aria-label="Jointed striped swimbait lure"></div>
        <span class="fav"><svg width="10" height="9" viewBox="0 0 10 9"><path d="M5 8.2 1.2 4.4a2.2 2.2 0 0 1 3.1-3.1L5 2l.7-.7a2.2 2.2 0 0 1 3.1 3.1z" fill="none" stroke="#555" stroke-width="1"/></svg></span></div>
      <div class="card-info"><h3 class="card-title">Swimbaits...</h3><p class="card-desc">Hunc vos beatum; Tria genera bonorum; Nam ista vestra: Si gravis, brevis;</p>
        <div class="card-buy"><span class="price">$20</span><span class="btn-cart">ADD TO CART</span><span class="btn-save">SAVE</span></div></div>
    </article>
    <article class="card">
      <div class="card-media"><span class="tag-pick"><b>★</b> STAFF PICK</span><span class="tag-date">MAR 11</span>
        <div class="product-photo" style="--tone:#2f5a3e;--tone-2:#b7d84e" role="img" aria-label="Green soft swimbait with chartreuse tail"></div>
        <span class="fav"><svg width="10" height="9" viewBox="0 0 10 9"><path d="M5 8.2 1.2 4.4a2.2 2.2 0 0 1 3.1-3.1L5 2l.7-.7a2.2 2.2 0 0 1 3.1 3.1z" fill="none" stroke="#555" stroke-width="1"/></svg></span></div>
      <div class="card-info"><h3 class="card-title">Umbrella Rigs...</h3><p class="card-desc">Is ita vivebat, ut nulla tam exquisita posset inveniri voluptas, qua non abundaret.</p>
        <div class="card-buy"><span class="price">$40</span><span class="btn-cart">ADD TO CART</span><span class="btn-save">SAVE</span></div></div>
    </article>
  </div>
</section>

<footer>
  <div class="footer-bar">
    <span>ABOUT US</span><span class="sep">|</span><span>PRODUCTS</span><span class="sep">|</span><span>OTHER</span>
    <div class="social"><span></span><span></span><span></span></div>
  </div>
  <p class="copyright">Copyright © 2018 tide-LOOP. - All Rights Reserved</p>
</footer>

</body>
</html>
```